Business card design for strategy and management consulting company. Would like to have a clean and professional business card, based on the attached logo. The company is a strategy and management consulting company focusing on sustainable business modlels based on economic, social and environmental market opportunities. Preferably the logo should be included on both sides of the design.

Industry/Entity Type

Business

Contact Information for Business Card

Håvard Lilleby, CEO/Management consultant
havard.lilleby@quarvenpartners.example
Mob: +47 948 26 317
Office: Vikfjell gate 14, pb 312 sentrum, N-0172 Oslo Norway

Requirements
Must have
• Include attached logo
Nice to have
• Would like to have the logo on both sides
Should not have
• Many colours.

```html
<!DOCTYPE html>
<html lang="en">
<head>
<meta charset="utf-8">
<title>Quarven business card</title>
<link rel="stylesheet" href="https://fonts.googleapis.com/css2?family=Questrial&display=swap">
<style>
  :root {
    --backdrop: #1c1c1c;
    --card: #0f0f0f;
    --ink: #ffffff;
    --accent: #f2d21a;
    --font: "Questrial", sans-serif;
  }
  * { margin: 0; padding: 0; box-sizing: border-box; }
  html, body {
    width: 1200px; height: 1200px; overflow: hidden;
    background: var(--backdrop);
    font-family: var(--font);
    color: var(--ink);
  }
  .card {
    position: absolute;
    left: 150px;
    width: 900px; height: 500px;
    background: var(--card);
    box-shadow: 0 10px 30px rgba(0,0,0,.5);
    overflow: hidden;
  }
  .card--front { top: 70px; }
  .card--back { top: 630px; }

  .brand {
    font-size: 118px; letter-spacing: -2px; line-height: 1;
    color: var(--ink);
    white-space: nowrap;
  }
  .card--front .brand {
    position: absolute; left: 50%; top: 50%;
    transform: translate(-50%, -50%);
  }
  .card--back .brand { position: absolute; left: 95px; top: 80px; }

  .rule {
    position: absolute; left: 0; right: 25px; top: 262px;
    height: 2px; background: var(--accent);
  }
  .person { position: absolute; left: 80px; top: 305px; }
  .person__name { font-size: 27px; text-transform: uppercase; letter-spacing: .5px; }
  .person__role { font-size: 22px; margin-top: 2px; }
  .address { position: absolute; left: 70px; top: 385px; font-size: 20px; line-height: 1.4; }

  .contact { position: absolute; left: 450px; top: 395px; font-size: 20px; }
  .contact__row { display: flex; align-items: center; gap: 12px; line-height: 1.5; white-space: nowrap; }
  .contact__icon { width: 24px; height: 18px; fill: var(--accent); flex: none; }
</style>
</head>
<body>
  <section class="card card--front">
    <div class="brand">Quarven</div>
  </section>

  <section class="card card--back">
    <div class="brand">Quarven</div>
    <div class="rule"></div>

    <div class="person">
      <p class="person__name">Håvard Lilleby</p>
      <p class="person__role">CEO/Management consultant</p>
    </div>
    <p class="address">Vikfjell gate 14<br>pb 312 sentrum, N-0172 Oslo Norway</p>

    <div class="contact">
      <p class="contact__row">
        <svg class="contact__icon" viewBox="0 0 26 20" aria-hidden="true">
          <path d="M2 6 C2 1 24 1 24 6 L24 8 L18 8 L18 5 L8 5 L8 8 L2 8 Z"/>
          <path d="M6 9 L20 9 L23 19 L3 19 Z"/>
        </svg>
        +47 948 26 317
      </p>
      <p class="contact__row">
        <svg class="contact__icon" viewBox="0 0 26 20" aria-hidden="true">
          <path d="M1 2 L25 2 L25 18 L1 18 Z M3 4 L13 12 L23 4 Z" fill-rule="evenodd"/>
        </svg>
        havard.lilleby@quarvenpartners.example
      </p>
    </div>
  </section>
</body>
</html>
```